Book Cover

Book Title: THE QUIET LEDGER
Book Sub Title: Notes on slowing the daily rush and shaping a calmer household rhythm
Vibe: Professional, stylish, trustworthy (high-end men's fashion)
Website (for inspiration): www.brindlequarry.com
Attached: a potential photo to use for the cover, but open to other options (from our website)

```html
<!DOCTYPE html>
<html lang="en">
<head>
<meta charset="utf-8">
<title>The Quiet Ledger — Book Cover</title>
<link rel="stylesheet" href="https://fonts.googleapis.com/css2?family=Bebas+Neue&display=swap">
<style>
  :root {
    --slate: #414f5c;
    --gold: #c4a777;
    --cream: #efe9da;
    --cream-light: #f4f0e5;
    --beam: #a89a84;
    --wall: #e4dccb;
    --wall-light: #efe9dc;
    --floor: #d6b68c;
    --floor-deep: #c49f72;
    --ink: #111111;
    --edge: #1d2533;
  }
  * { margin: 0; padding: 0; box-sizing: border-box; }
  html, body { width: 848px; height: 1200px; overflow: hidden; background: var(--cream); }
  .cover {
    position: relative;
    width: 848px;
    height: 1200px;
    overflow: hidden;
    font-family: "Bebas Neue", "Oswald", sans-serif;
    background: var(--cream);
  }
  .top-band {
    position: absolute; left: 0; top: 0;
    width: 100%; height: 39px;
    background: var(--slate);
  }
  .gold-rule {
    position: absolute; left: 0; top: 39px;
    width: 100%; height: 9px;
    background: var(--gold);
  }
  .cover-field {
    position: absolute; left: 0; top: 48px;
    width: 100%; height: 1088px;
    background: linear-gradient(90deg, var(--cream) 0%, var(--cream-light) 60%, var(--cream) 100%);
  }
  .hero-photo {
    position: absolute; left: 0; top: 48px;
    width: 560px; height: 1088px;
    background: linear-gradient(180deg,
      var(--beam) 0%,
      #c9bca6 15%,
      var(--wall) 24%,
      var(--wall-light) 48%,
      var(--wall) 60%,
      var(--floor) 75%,
      var(--floor-deep) 100%);
    -webkit-mask-image: linear-gradient(90deg, #000 0%, #000 72%, transparent 100%);
    mask-image: linear-gradient(90deg, #000 0%, #000 72%, transparent 100%);
  }
  .edge-shadow {
    position: absolute; right: 0; top: 48px;
    width: 22px; height: 1088px;
    background: linear-gradient(90deg, rgba(29,37,51,0) 0%, var(--edge) 70%);
  }
  .title {
    position: absolute; right: 30px; top: 304px;
    text-align: right;
    color: var(--gold);
    font-weight: 400;
  }
  .title span { display: block; }
  .title .lead { font-size: 100px; line-height: 90px; }
  .title .main { font-size: 240px; line-height: 222px; margin-top: 10px; }
  .title .tail { font-size: 100px; line-height: 90px; margin-top: 10px; }
  .subtitle {
    position: absolute; right: 30px; top: 910px;
    text-align: right;
    color: var(--ink);
    font-size: 46px;
    line-height: 56px;
  }
  .subtitle span { display: block; }
  .bottom-band {
    position: absolute; left: 0; bottom: 0;
    width: 100%; height: 64px;
    background: var(--slate);
    display: flex; align-items: center; justify-content: center;
  }
  .website {
    color: var(--gold);
    font-size: 40px;
    letter-spacing: 19px;
    padding-left: 19px;
  }
</style>
</head>
<body>
  <main class="cover">
    <div class="top-band"></div>
    <div class="gold-rule"></div>
    <div class="cover-field"></div>
    <div class="hero-photo" role="img" aria-label="Photo: a man in a navy suit seated on a wooden stool beside a clothing rack in a bright loft with wooden floors"></div>
    <div class="edge-shadow"></div>

    <h1 class="title">
      <span class="lead">THE</span>
      <span class="main">QUIET</span>
      <span class="tail">LEDGER</span>
    </h1>

    <p class="subtitle">
      <span>NOTES ON SLOWING THE</span>
      <span>DAILY RUSH AND SHAPING</span>
      <span>A CALMER HOUSEHOLD</span>
      <span>RHYTHM</span>
    </p>

    <footer class="bottom-band">
      <span class="website">WWW.BRINDLEQUARRY.COM</span>
    </footer>
  </main>
</body>
</html>
```